Vo Lunec - Business Cards & Stationnery
Think Ahead, Vo Lunec
Professional
Odile Fenwar Quintanel
48 rue des Glycines Doréales
75020 Paris
France
odile@volunec.com
www.volunec.com
The business cards have to be at the european standard ie 8,5 x 5,4 cm (seems to be 3.35'' x 2.13'')
Same for the stationnery ie A4 format, 21 x 29,7 cm (seems to be 8,27'' x 11.7'')
Please use the logo, name of the company and the base line: Think Ahead, Vo Lunec

```html
<!DOCTYPE html>
<html lang="fr">
<head>
<meta charset="utf-8">
<title>Vo Lunec – Business Cards</title>
<link rel="stylesheet" href="https://fonts.googleapis.com/css2?family=Montserrat:wght@400;500;700&family=Open+Sans:wght@400;600&display=swap">
<style>
  :root {
    --bg: #ecebef;
    --card: #ffffff;
    --purple: #5b2e86;
    --purple-light: #9a7bbd;
    --lilac: #e7e1ee;
    --ink: #2a2a2a;
    --grey: #6d6d6d;
    --faint: #ececf0;
  }
  * { margin: 0; padding: 0; box-sizing: border-box; }
  html, body { width: 1200px; height: 739px; overflow: hidden; }
  body {
    background: var(--bg);
    font-family: "Open Sans", sans-serif;
    color: var(--ink);
    position: relative;
  }
  .card {
    position: absolute;
    top: 198px;
    width: 540px;
    height: 343px;
    background: var(--card);
    box-shadow: 0 6px 18px rgba(0,0,0,.12);
    overflow: hidden;
  }
  .card--front { left: 40px; }
  .card--back { left: 620px; }

  /* front */
  .front-mark {
    position: absolute;
    left: 40px; top: 60px;
    width: 210px; height: 210px;
    background: var(--faint);
  }
  .front-wordmark {
    position: absolute;
    right: 40px; top: 140px;
    text-align: left;
  }
  .wordmark {
    font-family: "Montserrat", sans-serif;
    font-weight: 500;
    letter-spacing: 2px;
    color: var(--ink);
    text-transform: uppercase;
  }
  .front-wordmark .wordmark { font-size: 40px; line-height: 1; }
  .tagline {
    font-family: "Montserrat", sans-serif;
    font-weight: 400;
    text-transform: uppercase;
    color: var(--grey);
    letter-spacing: 1.6px;
  }
  .front-wordmark .tagline { font-size: 12px; margin-top: 6px; }

  /* back */
  .back-logo {
    position: absolute;
    left: 36px; top: 92px;
    width: 210px;
  }
  .back-logo .logo-square {
    width: 74px; height: 74px;
    background: var(--purple);
    margin: 0 0 14px 30px;
  }
  .back-logo .wordmark { font-size: 30px; line-height: 1; }
  .back-logo .tagline { font-size: 9px; margin-top: 5px; }
  .divider {
    position: absolute;
    left: 272px; top: 34px;
    width: 1px; height: 220px;
    background: var(--lilac);
  }
  .contact {
    position: absolute;
    left: 292px; top: 36px;
    right: 20px;
    font-size: 10.5px;
    line-height: 1.55;
    color: var(--grey);
  }
  .contact-name {
    font-family: "Open Sans", sans-serif;
    font-weight: 600;
    font-size: 12.5px;
    color: var(--purple);
    margin-bottom: 34px;
  }
  .contact-address { margin-bottom: 16px; }
  .contact-line {
    display: flex;
    align-items: center;
    gap: 8px;
    margin-bottom: 5px;
  }
  .contact-line svg { width: 13px; height: 13px; flex: none; }
  .band {
    position: absolute;
    left: 0; bottom: 0;
    width: 540px; height: 56px;
  }
</style>
</head>
<body>

  <section class="card card--front" aria-label="Recto de la carte">
    <div class="front-mark" aria-hidden="true"></div>
    <div class="front-wordmark">
      <div class="wordmark">Vo Lunec</div>
      <div class="tagline">Think Ahead, Vo Lunec</div>
    </div>
  </section>

  <section class="card card--back" aria-label="Verso de la carte">
    <div class="back-logo">
      <div class="logo-square" aria-hidden="true"></div>
      <div class="wordmark">Vo Lunec</div>
      <div class="tagline">Think Ahead, Vo Lunec</div>
    </div>

    <div class="divider" aria-hidden="true"></div>

    <div class="contact">
      <div class="contact-name">Odile Fenwar Quintanel</div>
      <div class="contact-address">48 rue des Glycines Doréales<br>75020 Paris, France</div>
      <div class="contact-line">
        <svg viewBox="0 0 14 14" aria-hidden="true"><circle cx="7" cy="7" r="7" fill="var(--purple)"/><path d="M4.6 3.6l1.4 1.4-.8 1c.5 1 1.3 1.8 2.3 2.3l1-.8 1.4 1.4-.9 1c-2.5-.4-4.9-2.8-5.3-5.3z" fill="#fff"/></svg>
        <span>+33 (0)6 00 47 18 93</span>
      </div>
      <div class="contact-line">
        <svg viewBox="0 0 14 14" aria-hidden="true"><circle cx="7" cy="7" r="7" fill="var(--purple)"/><rect x="3.5" y="4.6" width="7" height="4.8" fill="none" stroke="#fff" stroke-width=".9"/><path d="M3.5 4.6L7 7.3l3.5-2.7" fill="none" stroke="#fff" stroke-width=".9"/></svg>
        <span>odile@volunec.com</span>
      </div>
      <div class="contact-line">
        <svg viewBox="0 0 14 14" aria-hidden="true"><circle cx="7" cy="7" r="7" fill="var(--purple)"/><circle cx="7" cy="7" r="3.6" fill="none" stroke="#fff" stroke-width=".9"/><path d="M3.4 7h7.2M7 3.4c-1.6 2-1.6 5.2 0 7.2M7 3.4c1.6 2 1.6 5.2 0 7.2" fill="none" stroke="#fff" stroke-width=".7"/></svg>
        <span>www.volunec.com</span>
      </div>
    </div>

    <svg class="band" viewBox="0 0 540 56" preserveAspectRatio="none" aria-hidden="true">
      <polygon points="0,40 540,12 540,20 0,46" fill="var(--purple-light)"/>
      <polygon points="0,46 540,20 540,56 0,56" fill="var(--purple)"/>
      <rect x="470" y="4" width="30" height="20" fill="var(--purple)"/>
    </svg>
  </section>

</body>
</html>
```